Business card and insta posting square

This is for 2 separate projects...

1...a double sided business card for online business (no address) to hand to businesses to get them to list their details on my online directory. the butterfly logo is to be used on the business card.

2.... a posting square for Instagram to write inspirational quotes over the top of to post....with a small butterfly logo somewhere on it (in a corner maybe)....the square is to have a thin, solid green outline around the edge of it, and a faded picture through the background that will allow me to write text over the top of it that will be easily readable.
I would like the same box for all Instagram quote posts for consistency ..

Target Market(s)

spiritual , yoga, meditation, wellness......

Industry/Entity Type

Wellness

Contact Information for Business Card

Details for Business Card...
Tending A Bright Garden
Your Complete Wellness Directory
www.tendingabrightgarden.example
insta/FB/pinterest/twitter
*List Your Business for FREE *

Colors
33b8a4
34a7d8
3276b5
876aae
9bcb3c

Requirements
Must have
• butterfly logo included on business card
• insta post square can use the butterfly logo OR the TABG green square uploaded in the images
Nice to have
• greens

```html
<!DOCTYPE html>
<html lang="en">
<head>
<meta charset="utf-8">
<title>Tending A Bright Garden – Business Card</title>
<link href="https://fonts.googleapis.com/css2?family=Montserrat:wght@400;500;700&display=swap" rel="stylesheet">
<style>
  :root{
    --bg:#e9e7e3;
    --card:#fbfbfa;
    --gold:#d9ad2f;
    --gold-light:#f3d778;
    --green:#2f9a3f;
    --green-soft:#9bcb3c;
    --line-green:#8cc58a;
    --teal:#33b8a4;
    --blue:#3276b5;
    --sky:#34a7d8;
    --purple:#876aae;
    --deep-purple:#5a2f9a;
  }
  *{box-sizing:border-box;margin:0;padding:0}
  html,body{width:1200px;height:900px;overflow:hidden}
  body{background:var(--bg);font-family:"Montserrat",sans-serif;position:relative}

  .card{
    position:absolute;left:290px;width:620px;height:355px;
    background:var(--card);
    border:7px solid var(--gold);
    box-shadow:inset 0 0 0 2px var(--gold-light),0 10px 24px rgba(0,0,0,.15);
    overflow:hidden;
  }
  .card--back{top:50px}
  .card--front{top:480px}

  .brand-mark{display:flex;flex-direction:column;align-items:center}
  .brand-mark__dot{
    width:58px;height:58px;border-radius:50%;
    background:linear-gradient(135deg,var(--sky),var(--purple));
    margin-bottom:10px;
  }
  .brand-mark__name{
    font-weight:500;font-size:19px;color:var(--green);white-space:nowrap;
  }

  /* back side */
  .card--back .brand-mark{position:absolute;top:40px;left:0;right:0}
  .note-lines{position:absolute;left:80px;right:60px;top:190px}
  .note-lines span{display:block;height:1px;background:var(--line-green);margin-bottom:32px}

  /* front side */
  .front-brand{position:absolute;left:24px;top:90px;width:226px}
  .front-brand .brand-mark__name{font-size:16px}
  .tagline{margin-top:10px;text-align:center;font-size:11px;font-weight:500;color:var(--green);white-space:nowrap}
  .divider{position:absolute;left:268px;top:82px;width:2px;height:150px;background:var(--deep-purple)}
  .contact{position:absolute;left:288px;top:80px;right:14px}
  .contact__name{
    font-weight:700;font-size:24px;line-height:1;
    background:linear-gradient(90deg,var(--deep-purple),var(--blue) 50%,var(--green-soft));
    -webkit-background-clip:text;background-clip:text;color:transparent;display:inline-block;
  }
  .contact__role{font-size:16px;font-weight:500;color:var(--green);margin-top:2px}
  .social{display:flex;gap:5px;margin:8px 0 10px}
  .social span{width:20px;height:20px;border-radius:50%;background:var(--teal)}
  .contact__row{display:flex;align-items:center;gap:7px;font-size:17px;font-weight:500;color:var(--green);margin-bottom:4px;white-space:nowrap}
  .contact__row svg{flex:none}
  .contact__row--url{font-size:13.5px;letter-spacing:-0.1px}
  .contact__cta{font-size:17px;font-weight:500;color:var(--green);margin-top:2px;white-space:nowrap}
</style>
</head>
<body>

  <section class="card card--back" aria-label="Card back">
    <div class="brand-mark">
      <div class="brand-mark__dot"></div>
      <div class="brand-mark__name">Tending A Bright Garden</div>
    </div>
    <div class="note-lines"><span></span><span></span><span></span></div>
  </section>

  <section class="card card--front" aria-label="Card front">
    <div class="front-brand">
      <div class="brand-mark">
        <div class="brand-mark__dot"></div>
        <div class="brand-mark__name">Tending A Bright Garden</div>
      </div>
      <p class="tagline">Your Complete Wellness Directory</p>
    </div>

    <div class="divider"></div>

    <div class="contact">
      <h1 class="contact__name">Alex Rowan</h1>
      <p class="contact__role">Manager</p>
      <div class="social" aria-label="Social profiles"><span></span><span></span><span></span><span></span></div>
      <p class="contact__row">
        <svg width="16" height="16" viewBox="0 0 24 24" aria-hidden="true"><path fill="var(--blue)" d="M6.6 10.8a15.1 15.1 0 0 0 6.6 6.6l2.2-2.2a1 1 0 0 1 1-.25 11.4 11.4 0 0 0 3.6.57 1 1 0 0 1 1 1V20a1 1 0 0 1-1 1A17 17 0 0 1 3 4a1 1 0 0 1 1-1h3.5a1 1 0 0 1 1 1c0 1.25.2 2.45.57 3.57a1 1 0 0 1-.25 1z"/></svg>
        555-014-2100
      </p>
      <p class="contact__row contact__row--url">
        <svg width="16" height="16" viewBox="0 0 24 24" aria-hidden="true"><circle cx="12" cy="12" r="10" fill="var(--sky)"/><path d="M2 12h20M12 2c3 3 3 17 0 20M12 2c-3 3-3 17 0 20" stroke="#fff" stroke-width="1.5" fill="none"/></svg>
        www.tendingabrightgarden.example
      </p>
      <p class="contact__cta">List Your Business for FREE</p>
    </div>
  </section>

</body>
</html>
```